Travel video blogger needs website design

I need a website designed for my new travel video blog "Roaming Sparrow". I have only just started but need a website that is fairly simple and not too busy. I have a logo which I want on it (I have attached it to this project). I also want a link to all my other social medias on the main page (vidtrekhub, Snapwell and Palnook) and my videos as well. Here is a link to my vidtrekhub page for you to look at: https://www.vidtrekhub.net/channel/QRm4tZ8pWnE2HX57YKccd31v
As I have only just started and I am still trying to find my specific niche, again I need it to be sleek and simple that I can go in and change slightly here and there. I would like these pages on the website: About Me, Videos, Social Media, Blog, Gallery, contact me. for an example I like the look of www.theroamingkinfolk.net website.

I already have the domain and I am with Harborweb with pagecraftr.org. I just want to spend my time getting better and learning about videos then trying to create a website (I am a bit of a perfectionist when I try to do something).

Target Market(s)

Young Adults (majority females) between the ages of 18 and 30 with an interest in travelling.

Industry/Entity Type

Travel Industry

Number of Pages Required

1 page

Colors

Designer to choose colors to be used in the design.

Requirements
Must have
• A like to my Snapwell, Palnook and vidtrekhub channels on the home page
• Must be a nice, simple design
• Must have my logo on the front and name "Roaming Sparrow"
Nice to have
• A nice light, bright coloured theme
Should not have
• A dark coloured theme

```html
<!DOCTYPE html>
<html lang="en">
<head>
<meta charset="utf-8">
<title>Roaming Sparrow — Travel Blog</title>
<link href="https://fonts.googleapis.com/css2?family=Montserrat:wght@400;500;700&family=Playfair+Display:wght@700&display=swap" rel="stylesheet">
<style>
:root{
  --sand:#e2b982;
  --sand-light:#ebc99c;
  --ink:#1d1d1d;
  --muted:#8b8b8b;
  --body:#6f6f6f;
  --white:#ffffff;
  --heart:#f08aa0;
  --serif:'Playfair Display', Georgia, serif;
  --sans:'Montserrat', Arial, sans-serif;
}
*{margin:0;padding:0;box-sizing:border-box}
html,body{width:1200px;height:2927px;overflow:hidden;background:var(--white);font-family:var(--sans);color:var(--ink)}
.page{position:relative;width:1200px;height:2927px}
.hero-panel{position:absolute;left:0;top:0;width:751px;height:675px;background:var(--sand);z-index:0}
.hero-photo{position:absolute;left:447px;top:119px;width:630px;height:439px;background:linear-gradient(100deg,#d9cbb6 0%,#e8dccb 40%,#cfa772 62%,#6f7d96 100%);box-shadow:0 10px 30px rgba(0,0,0,.25);z-index:1}
.hero-copy{position:absolute;left:123px;top:292px;width:600px;z-index:2}
.brand{position:absolute;left:110px;top:46px;display:flex;align-items:center;gap:8px;font-family:var(--sans);font-weight:700;font-size:15px;color:var(--ink);letter-spacing:.5px;text-transform:uppercase;z-index:2}
.brand-dot{width:14px;height:14px;border-radius:50%;background:var(--white)}
.menu-toggle{position:absolute;left:1147px;top:16px;z-index:2}
.hero-title{font-family:var(--serif);font-weight:700;font-size:55px;line-height:60px;color:var(--ink);width:560px}
.hero-sub{margin-top:14px;font-size:21px;color:var(--white)}
.scroll-cue{position:absolute;left:566px;top:588px;width:70px;text-align:center;font-size:17px;color:var(--white);z-index:2}
.scroll-cue svg{display:block;margin:8px auto 0}
.post{position:absolute;width:404px}
.post-date{position:absolute;left:-46px;top:0;transform:rotate(-90deg) translateX(-100%);transform-origin:0 0;font-size:11px;letter-spacing:1px;color:var(--muted);text-transform:uppercase;white-space:nowrap}
.post-media{width:404px;height:509px;box-shadow:0 6px 18px rgba(0,0,0,.18)}
.post-title{position:absolute;left:0;top:378px;width:351px;height:88px;background:var(--white);display:flex;align-items:center;padding:0 18px;font-family:var(--serif);font-weight:700;font-size:24px;line-height:32px;color:var(--ink)}
.post-meta{margin-top:22px;font-size:12px;color:var(--muted);text-transform:uppercase;display:flex;align-items:center;gap:10px}
.post-meta b{color:var(--ink)}
.post-meta .sep{font-size:14px}
.post-meta .likes{display:flex;align-items:center;gap:6px}
.post-excerpt{margin-top:18px;font-size:15px;line-height:23px;color:var(--body);width:390px}
.read-more{display:inline-block;margin-top:28px;font-weight:700;font-size:15px;letter-spacing:.5px;color:var(--ink);text-decoration:none;padding-bottom:6px;border-bottom:3px solid var(--sand)}
.social-band{position:absolute;left:0;top:2361px;width:1200px;height:87px;background:var(--sand-light);display:flex;justify-content:center;align-items:center;gap:58px}
.social-link{display:flex;align-items:center;gap:10px;font-size:18px;color:var(--ink);text-decoration:none}
.social-mark{width:12px;height:12px;background:var(--ink)}
.gallery{position:absolute;left:0;top:2448px;width:1200px;height:242px;display:flex}
.gallery-tile{flex:1;height:100%}
.follow{position:absolute;left:425px;top:2657px;width:350px;height:68px;background:var(--white);display:flex;align-items:center;justify-content:center;font-family:var(--serif);font-weight:700;font-size:24px;box-shadow:0 6px 18px rgba(0,0,0,.12)}
.copyright{position:absolute;left:123px;top:2811px;font-size:15px;color:var(--muted)}
.back-top{position:absolute;left:935px;top:2809px;font-size:15px;letter-spacing:1.5px;color:var(--muted);display:flex;align-items:center;gap:12px;text-decoration:none}
</style>
</head>
<body>
<div class="page">
  <header class="hero-panel"></header>
  <div class="brand"><span class="brand-dot"></span>Roaming Sparrow</div>
  <svg class="menu-toggle" width="36" height="24" viewBox="0 0 36 24"><path d="M0 2H36M6 12H36M0 22H36" stroke="#1d1d1d" stroke-width="2.5"/></svg>
  <div class="hero-photo" role="img" aria-label="Blogger smiling on a sandy beach"></div>
  <div class="hero-copy">
    <h1 class="hero-title">Take a dream of traveling the world</h1>
    <p class="hero-sub">and turn it into reality</p>
  </div>
  <div class="scroll-cue">Scroll
    <svg width="38" height="20" viewBox="0 0 38 20"><path d="M2 2 L19 18 L36 2" fill="none" stroke="#fff" stroke-width="2.5"/></svg>
  </div>

  <article class="post" style="left:168px;top:763px">
    <span class="post-date">12 August, 2018</span>
    <div class="post-media" role="img" aria-label="Aerial performer on a rope under blue stage light" style="background:linear-gradient(160deg,#0a2fb0,#1e6de0 50%,#081c7a)"></div>
    <h2 class="post-title">The Grand Ringmaster</h2>
    <div class="post-meta">By <b>Tessa</b><span class="sep">·</span>5 min read<span class="sep">·</span><span class="likes"><svg width="14" height="12" viewBox="0 0 14 12"><path d="M7 11 L1.5 5.5 A3 3 0 0 1 7 2 A3 3 0 0 1 12.5 5.5 Z" fill="none" stroke="var(--heart)" stroke-width="1.3"/></svg>389</span></div>
    <p class="post-excerpt">Lorem ipsum dolor sit amet, consectetur adipiscing elit. In eu dictum felis. In elementum semper nisi sed condimentum. Phasellus commodo nisi luctus, ornare nulla sit</p>
    <a class="read-more" href="#">READ MORE</a>
  </article>

  <article class="post" style="left:673px;top:763px">
    <span class="post-date">12 August, 2018</span>
    <div class="post-media" role="img" aria-label="Two children looking into a circus tent" style="background:linear-gradient(180deg,#d8d8d8 0%,#2a2c3a 30%,#4a4038 65%,#c8473a 100%)"></div>
    <h2 class="post-title">What did I do this week?</h2>
    <div class="post-meta">By <b>Tessa</b><span class="sep">·</span>5 min read<span class="sep">·</span><span class="likes"><svg width="14" height="12" viewBox="0 0 14 12"><path d="M7 11 L1.5 5.5 A3 3 0 0 1 7 2 A3 3 0 0 1 12.5 5.5 Z" fill="none" stroke="var(--heart)" stroke-width="1.3"/></svg>389</span></div>
    <p class="post-excerpt">Lorem ipsum dolor sit amet, consectetur adipiscing elit. In eu dictum felis. In elementum semper nisi sed condimentum. Phasellus commodo nisi luctus, ornare nulla sit</p>
    <a class="read-more" href="#">READ MORE</a>
  </article>

  <article class="post" style="left:168px;top:1545px">
    <span class="post-date">12 August, 2018</span>
    <div class="post-media" role="img" aria-label="Rocky coastal cliff and rock shelf" style="background:linear-gradient(180deg,#d9dde0 0%,#5b4f40 25%,#7a6a58 60%,#3b3530 100%)"></div>
    <h2 class="post-title">Can you take a guess of where I'm going to be?</h2>
    <div class="post-meta">By <b>Tessa</b><span class="sep">·</span>5 min read<span class="sep">·</span><span class="likes"><svg width="14" height="12" viewBox="0 0 14 12"><path d="M7 11 L1.5 5.5 A3 3 0 0 1 7 2 A3 3 0 0 1 12.5 5.5 Z" fill="none" stroke="var(--heart)" stroke-width="1.3"/></svg>389</span></div>
    <p class="post-excerpt">Lorem ipsum dolor sit amet, consectetur adipiscing elit. In eu dictum felis. In elementum semper nisi sed condimentum. Phasellus commodo nisi luctus, ornare nulla sit</p>
    <a class="read-more" href="#">READ MORE</a>
  </article>

  <article class="post" style="left:673px;top:1545px">
    <span class="post-date">12 August, 2018</span>
    <div class="post-media" role="img" aria-label="Woman on a beach by the sea under blue sky" style="background:linear-gradient(180deg,#2f74d0 0%,#6aa6e6 35%,#1f5fa8 38%,#b8a890 55%,#d8c8b0 100%)"></div>
    <h2 class="post-title">Welcome To The Family!</h2>
    <div class="post-meta">By <b>Tessa</b><span class="sep">·</span>5 min read<span class="sep">·</span><span class="likes"><svg width="14" height="12" viewBox="0 0 14 12"><path d="M7 11 L1.5 5.5 A3 3 0 0 1 7 2 A3 3 0 0 1 12.5 5.5 Z" fill="none" stroke="var(--heart)" stroke-width="1.3"/></svg>389</span></div>
    <p class="post-excerpt">Lorem ipsum dolor sit amet, consectetur adipiscing elit. In eu dictum felis. In elementum semper nisi sed condimentum. Phasellus commodo nisi luctus, ornare nulla sit</p>
    <a class="read-more" href="#">READ MORE</a>
  </article>

  <nav class="social-band">
    <a class="social-link" href="https://www.vidtrekhub.net/channel/QRm4tZ8pWnE2HX57YKccd31v"><span class="social-mark"></span>vidtrekhub</a>
    <a class="social-link" href="#"><span class="social-mark"></span>Snapwell</a>
    <a class="social-link" href="#"><span class="social-mark"></span>Palnook</a>
  </nav>
  <section class="gallery">
    <div class="gallery-tile" role="img" aria-label="Beach portrait of the blogger" style="background:linear-gradient(120deg,#d8cfc2,#cfa772 60%,#7c8aa3)"></div>
    <div class="gallery-tile" role="img" aria-label="Children at a circus tent" style="background:linear-gradient(180deg,#dcdcdc,#2a2c3a 40%,#c8473a)"></div>
    <div class="gallery-tile" role="img" aria-label="Aerial performer in blue light" style="background:linear-gradient(160deg,#0a2fb0,#1e6de0 50%,#081c7a)"></div>
    <div class="gallery-tile" role="img" aria-label="Sunset over a rocky shore" style="background:linear-gradient(180deg,#8d8a94,#e8b870 45%,#3a342e)"></div>
    <div class="gallery-tile" role="img" aria-label="Woman on a sunny beach" style="background:linear-gradient(180deg,#2f74d0,#6aa6e6 38%,#c9b89e)"></div>
  </section>
  <div class="follow">Follow me on Snapwell</div>

  <footer>
    <p class="copyright">Copyright © 2018 Roaming Sparrow.</p>
    <a class="back-top" href="#">BACK TO TOP
      <svg width="14" height="9" viewBox="0 0 14 9"><path d="M1 8 L7 2 L13 8" fill="none" stroke="#8b8b8b" stroke-width="2"/></svg>
    </a>
  </footer>
</div>
</body>
</html>
```